Business Card Design Project

We need a hip business card! We are a bakery that specializes in bite sized treats! We do not like foo-foo things, rather have a hip, edgy nature about our style. Our head baker has lots of tattoos....basically, we are not going for the tea party look. We have uploaded our logo, which has a character in it...because we still want to be fun and friendly to little peeps...

Colors: Red and Black
Use : Existing logo
Info: name, address, telephone #, email, URL

Industry/Entity Type

Bakery

Requirements
Must have
• logo: will upload
font: serfiffic grunge
feel: hip and cool, somewhat edgy yet still fun

```html
<!DOCTYPE html>
<html lang="en">
<head>
<meta charset="utf-8">
<title>Crumbly Business Card</title>
<link rel="stylesheet" href="https://fonts.googleapis.com/css2?family=Chelsea+Market&display=swap">
<style>
  :root {
    --card-white: #ffffff;
    --card-black: #0b0b0c;
    --accent-red: #e8231f;
    --ink-black: #141414;
  }
  html, body {
    margin: 0;
    padding: 0;
    overflow: hidden;
    background: var(--card-white);
  }
  .card {
    position: relative;
    width: 1200px;
    height: 676px;
    overflow: hidden;
    background: var(--card-white);
    font-family: "Chelsea Market", "Georgia", serif;
  }
  .card__panel {
    position: absolute;
    inset: 0;
  }
  .brand {
    position: absolute;
    left: 100px;
    top: 96px;
    display: flex;
    align-items: center;
    gap: 22px;
  }
  .brand__mark {
    width: 96px;
    height: 96px;
    border-radius: 50%;
    background: var(--accent-red);
  }
  .brand__name {
    font-size: 50px;
    line-height: 1;
    color: var(--ink-black);
    letter-spacing: 1px;
  }
  .contact {
    position: absolute;
    right: 91px;
    top: 96px;
    margin: 0;
    text-align: right;
    color: var(--accent-red);
    font-size: 40px;
    line-height: 1.15;
  }
  .contact__item {
    margin: 0 0 46px;
  }
  .contact__item--address {
    margin-bottom: 48px;
  }
</style>
</head>
<body>
  <div class="card">
    <svg class="card__panel" width="1200" height="676" viewBox="0 0 1200 676" aria-hidden="true">
      <rect x="612" y="0" width="588" height="676" fill="var(--card-black)"/>
      <g fill="var(--card-black)">
        <circle cx="612" cy="0" r="25"/>
        <circle cx="612" cy="49" r="25"/>
        <circle cx="612" cy="98" r="25"/>
        <circle cx="612" cy="147" r="25"/>
        <circle cx="612" cy="196" r="25"/>
        <circle cx="612" cy="245" r="25"/>
        <circle cx="612" cy="294" r="25"/>
        <circle cx="612" cy="343" r="25"/>
        <circle cx="612" cy="392" r="25"/>
        <circle cx="612" cy="441" r="25"/>
        <circle cx="612" cy="490" r="25"/>
        <circle cx="612" cy="539" r="25"/>
        <circle cx="612" cy="588" r="25"/>
        <circle cx="612" cy="637" r="25"/>
        <circle cx="612" cy="686" r="25"/>
      </g>
    </svg>

    <div class="brand">
      <div class="brand__mark"></div>
      <span class="brand__name">CRUMBLY</span>
    </div>

    <address class="contact">
      <p class="contact__item">Mara Sample</p>
      <p class="contact__item contact__item--address">#31 Oven St.,<br>Cebu, PH</p>
      <p class="contact__item">09 555 013 276</p>
      <p class="contact__item">crumbly@mail.com</p>
      <p class="contact__item">.url</p>
    </address>
  </div>
</body>
</html>
```